New Webpage for High Class Expert Witness Services Company

We are looking for a minimalist design for a webpage that just has our logo and an entry form offer to connect with one of our Liaisons.
The entry form should just ask for Name, Email, Contact Info and Description of Project.

Company Name is: The Marlow Crest Advisory Services

Number of Pages Required

1 page

```html
<!DOCTYPE html>
<html lang="en">
<head>
<meta charset="utf-8">
<title>The Marlow Crest Advisory Services — Liaison Connect</title>
<link href="https://fonts.googleapis.com/css2?family=Gelasio:wght@400;600;700&display=swap" rel="stylesheet">
<style>
  :root {
    --page-bg: #121315;
    --card-bg: #171a1c;
    --card-border: #25282b;
    --field-bg: #0f1012;
    --field-border: #2a2c2f;
    --rule: #2a2c2f;
    --text-strong: #c4c4c4;
    --text-body: #6f7174;
    --text-label: #5d5f62;
    --text-faint: #3e4043;
    --button-border: #4a4c4f;
  }
  * { box-sizing: border-box; margin: 0; padding: 0; }
  html, body {
    width: 1200px; height: 1200px; overflow: hidden;
    background: var(--page-bg);
    font-family: "Gelasio", Georgia, serif;
    color: var(--text-strong);
  }
  .page { position: relative; width: 1200px; height: 1200px; }

  .brand { position: absolute; left: 327px; top: 77px; display: flex; align-items: center; }
  .brand-mark {
    width: 54px; height: 54px; border: 1.5px solid #3e4043; border-radius: 50%;
    margin-right: 35px;
  }
  .brand-divider { width: 1px; height: 60px; background: #3e4043; margin-right: 29px; }
  .brand-name {
    font-size: 29px; font-weight: 700; letter-spacing: 3.2px; line-height: 1;
    color: var(--text-strong);
  }
  .brand-sub {
    display: flex; align-items: center; margin-top: 6px;
    font-size: 13px; letter-spacing: 5.6px; color: #8b8c8e;
  }
  .brand-sub::before, .brand-sub::after {
    content: ""; width: 24px; height: 1px; background: #6f7174;
  }
  .brand-sub::before { margin-right: 10px; }
  .brand-sub::after { margin-left: 5px; }
  .brand-tagline {
    margin-top: 6px; font-size: 11.5px; letter-spacing: 5.2px; color: #5d5f62;
  }

  .header-rule { position: absolute; left: 176px; top: 176px; width: 847px; height: 1px; background: var(--rule); }

  .intro { position: absolute; left: 0; top: 236px; width: 1200px; text-align: center; }
  .eyebrow { font-size: 12px; letter-spacing: 5.5px; color: var(--text-label); }
  .headline { margin-top: 17px; font-size: 34px; font-weight: 400; color: var(--text-strong); }
  .lede { margin: 18px auto 0; width: 600px; font-size: 16px; line-height: 27px; color: var(--text-body); letter-spacing: 0.2px; }
  .intro-rule { position: absolute; left: 571px; top: 461px; width: 58px; height: 1px; background: #3a3c3f; }

  .liaison-card {
    position: absolute; left: 260px; top: 496px; width: 680px; height: 539px;
    background: var(--card-bg); border: 1px solid var(--card-border); border-radius: 3px;
  }
  .card-title {
    position: absolute; left: 0; top: 42px; width: 100%; text-align: center;
    font-size: 12px; letter-spacing: 5.5px; color: var(--text-faint);
  }
  .field { position: absolute; }
  .field-label {
    display: block; font-size: 12px; letter-spacing: 4.2px; color: var(--text-label);
    margin-bottom: 9px; line-height: 1;
  }
  .field-input {
    width: 100%; height: 45px; background: var(--field-bg); border: 1px solid var(--field-border);
    border-radius: 2px; padding: 0 17px;
    font-family: "Gelasio", Georgia, serif; font-size: 16px; color: var(--text-strong);
  }
  .field-input::placeholder { color: #a9aaab; }
  textarea.field-input { height: 112px; padding: 12px 17px; resize: vertical; line-height: 1.4; }

  .field-name { left: 49px; top: 89px; width: 280px; }
  .field-email { left: 349px; top: 89px; width: 280px; }
  .field-contact { left: 49px; top: 183px; width: 580px; }
  .field-project { left: 49px; top: 277px; width: 580px; }

  .submit-button {
    position: absolute; left: 154px; top: 448px; width: 370px; height: 47px;
    background: transparent; border: 1px solid var(--button-border); border-radius: 2px;
    font-family: "Gelasio", Georgia, serif; font-size: 13px; letter-spacing: 5.5px;
    color: #b3b4b5;
  }

  .footer {
    position: absolute; left: 0; top: 1091px; width: 1200px; text-align: center;
    font-size: 12px; letter-spacing: 4.5px; color: var(--text-faint);
  }
</style>
</head>
<body>
<div class="page">
  <header class="brand">
    <span class="brand-mark"></span>
    <span class="brand-divider"></span>
    <div class="brand-text">
      <div class="brand-name">MARLOW CREST</div>
      <div class="brand-sub">ADVISORY SERVICES</div>
      <div class="brand-tagline">SEAMLESS MEDICAL EXPERT INTEGRATION</div>
    </div>
  </header>
  <div class="header-rule"></div>

  <section class="intro">
    <p class="eyebrow">LIAISON CONNECT</p>
    <h1 class="headline">Speak with a Marlow Crest Liaison</h1>
    <p class="lede">Our specialists are ready to support your mission. Complete the form below and a dedicated liaison will reach out within 24 hours.</p>
  </section>
  <div class="intro-rule"></div>

  <form class="liaison-card">
    <p class="card-title">SECURE ENTRY FORM</p>
    <label class="field field-name">
      <span class="field-label">FULL NAME</span>
      <input class="field-input" type="text" placeholder="John R. Smith">
    </label>
    <label class="field field-email">
      <span class="field-label">EMAIL ADDRESS</span>
      <input class="field-input" type="email" placeholder="your@domain.com">
    </label>
    <label class="field field-contact">
      <span class="field-label">CONTACT INFORMATION</span>
      <input class="field-input" type="text" placeholder="Phone number or preferred contact method">
    </label>
    <label class="field field-project">
      <span class="field-label">DESCRIPTION OF PROJECT</span>
      <textarea class="field-input" placeholder="Briefly describe your project, operational needs, or area of inquiry..."></textarea>
    </label>
    <button class="submit-button" type="button">REQUEST A LIAISON &nbsp;→</button>
  </form>

  <footer class="footer">© 2026 &nbsp;· &nbsp;THE MARLOW CREST ADVISORY SERVICES &nbsp;· &nbsp;CONFIDENTIAL</footer>
</div>
</body>
</html>
```